CBDI Root Beer bottle label design.

We produce homemade root beer the same way since 1965. Family owned and third generation owner. The root beer will bring you back 50 years. This will go on a brown beer bottle. Our website is www.corvalebaydrivein.com. We have a logo on our website but I would like something different. we are a 50's style drive in restaurant like K&J and Velda. I would like this to be a new logo for our business.

Target Market(s)

All ages

Colors
f37122
ffffff
000000

Requirements
Must have
• Easy to read. Retro style font with a lot of white in the logo. I would like to be able to pull the logo out separately and put that just on the bottle if I choose. I added some examples of labels and the style of font I like.

```html
<!DOCTYPE html>
<html lang="en">
<head>
<meta charset="utf-8">
<title>CBDI Root Beer Label</title>
<link rel="stylesheet" href="https://fonts.googleapis.com/css2?family=Rye&family=Josefin+Sans:wght@600&display=swap">
<style>
  :root {
    --backdrop: #e9e6e6;
    --label: #2a2a2b;
    --label-stripe: #323233;
    --oval-fill: #111111;
    --orange: #f37122;
    --orange-deep: #c9561a;
    --white: #ffffff;
    --cream: #f2efe9;
    --star: #6a6a6a;
  }
  * { box-sizing: border-box; margin: 0; padding: 0; }
  html, body { width: 802px; height: 1200px; overflow: hidden; }
  body {
    background: var(--backdrop);
    position: relative;
    font-family: "Josefin Sans", sans-serif;
  }
  .neck-label {
    position: absolute;
    left: 251px;
    top: 60px;
    width: 300px;
    height: 130px;
    background: var(--label);
    display: flex;
    align-items: center;
    justify-content: center;
  }
  .brand-name {
    font-family: "Josefin Sans", sans-serif;
    font-weight: 600;
    color: var(--cream);
    letter-spacing: 2px;
    white-space: nowrap;
  }
  .neck-label .brand-name { font-size: 28px; }
  .body-label {
    position: absolute;
    left: 131px;
    top: 260px;
    width: 540px;
    height: 880px;
    background:
      repeating-linear-gradient(90deg, var(--label) 0 9px, var(--label-stripe) 9px 11px);
  }
  .emblem {
    position: absolute;
    left: 0;
    top: 0;
    width: 540px;
    height: 880px;
  }
  .product-name {
    position: absolute;
    left: 0;
    width: 540px;
    top: 300px;
    text-align: center;
    font-family: "Rye", serif;
    font-size: 112px;
    line-height: 1.12;
    color: var(--cream);
    letter-spacing: -2px;
  }
  .body-label .brand-name {
    position: absolute;
    left: 0;
    width: 540px;
    top: 762px;
    text-align: center;
    font-size: 34px;
  }
</style>
</head>
<body>
  <div class="neck-label">
    <span class="brand-name">CORVALE BAY</span>
  </div>

  <div class="body-label">
    <svg class="emblem" viewBox="0 0 540 880" aria-hidden="true">
      <defs>
        <linearGradient id="ovalRing" x1="0" y1="0" x2="0" y2="1">
          <stop offset="0" stop-color="var(--orange)"/>
          <stop offset="1" stop-color="var(--orange-deep)"/>
        </linearGradient>
      </defs>
      <ellipse class="oval" cx="270" cy="433" rx="212" ry="296" fill="var(--oval-fill)" stroke="url(#ovalRing)" stroke-width="7"/>
      <g class="stars" fill="var(--star)">
        <polygon points="223,233 227,244 239,244 229,251 233,262 223,255 213,262 217,251 207,244 219,244"/>
        <polygon points="270,226 274,237 286,237 276,244 280,255 270,248 260,255 264,244 254,237 266,237"/>
        <polygon points="317,233 321,244 333,244 323,251 327,262 317,255 307,262 311,251 301,244 313,244"/>
      </g>
    </svg>
    <h1 class="product-name">ROOT<br>BEER</h1>
    <span class="brand-name">CORVALE BAY</span>
  </div>
</body>
</html>
```